Harborline Crest Insurance Services

we are a high end insurance agency we specialize on Auto | Home | Business | Life looking for something professional and luxuries at the same time. if you guys need anything else please let me know.

Auto | Home | Business | Life must be under logo on the back with black background.

i want the back part to be black with our gold logo on it.

Target Market(s)

Auto | Home | Business | Life

Industry/Entity Type

Insurance Broker

Contact Information for Business Card

My logo is gold so a black in the back would be nice.

Font styles to use
Serif

Colors
000000

Requirements
Must have
• Big logo on the back with black background.

```html
<!DOCTYPE html>
<html lang="en">
<head>
<meta charset="utf-8">
<title>Harborline Crest Insurance Services — Business Card</title>
<link href="https://fonts.googleapis.com/css2?family=Noto+Serif:wght@400;600&family=Roboto:ital,wght@0,400;1,400&display=swap" rel="stylesheet">
<style>
  :root {
    --backdrop: #e4e4e4;
    --card: #0b0b0d;
    --gold: #d9ad2b;
    --silver: #b9b9bb;
    --text-light: #e8e8e8;
    --text-muted: #cfcfcf;
  }
  * { box-sizing: border-box; margin: 0; padding: 0; }
  html, body {
    width: 1200px; height: 576px; overflow: hidden;
    background: var(--backdrop);
  }
  .canvas { position: relative; width: 1200px; height: 576px; }

  .card {
    position: absolute;
    width: 484px; height: 294px;
    background: var(--card);
    border-radius: 11px;
    box-shadow: 2px 4px 8px rgba(0,0,0,0.35);
    overflow: hidden;
  }
  .card--back { left: 82px; top: 138px; }
  .card--front { left: 602px; top: 138px; width: 482px; height: 291px; }

  .brand {
    position: absolute;
    text-align: center;
    font-family: "Noto Serif", serif;
    font-weight: 600;
    color: var(--gold);
    line-height: 1.15;
  }
  .brand__dot {
    display: block;
    margin: 0 auto 10px;
    border-radius: 50%;
    background: var(--gold);
  }
  .card--back .brand { left: 0; width: 484px; top: 96px; font-size: 22px; }
  .card--back .brand__dot { width: 40px; height: 40px; }
  .brand__sub { display: block; font-size: 0.55em; letter-spacing: 0.2em; text-transform: uppercase; margin-top: 3px; }

  .services {
    position: absolute; left: 0; right: 0; top: 265px;
    display: flex; align-items: center;
  }
  .services__band { height: 5px; background: var(--gold); }
  .services__band--left { width: 146px; }
  .services__band--right { flex: 1; }
  .services__list {
    width: 192px; text-align: center;
    font-family: "Roboto", sans-serif; font-size: 13px;
    color: var(--text-light);
  }

  .card__tab {
    position: absolute; left: 0; top: 32px; width: 14px; height: 37px;
    background: linear-gradient(90deg, #8d8d8f, #e2e2e4 50%, #9a9a9c);
  }
  .person { position: absolute; left: 27px; top: 32px; }
  .person__name {
    font-family: "Noto Serif", serif; font-weight: 400;
    font-size: 21px; color: var(--gold); letter-spacing: 0.02em;
  }
  .person__role {
    font-family: "Roboto", sans-serif; font-style: italic;
    font-size: 11px; color: var(--text-light); margin-top: 2px;
  }
  .card--front .brand { left: 268px; width: 200px; top: 62px; font-size: 17px; }
  .card--front .brand__dot { width: 32px; height: 32px; margin-bottom: 8px; }

  .contact {
    position: absolute; left: 27px; top: 206px;
    font-family: "Roboto", sans-serif; font-size: 11.5px;
    color: var(--text-light); list-style: none;
  }
  .contact__item { display: flex; align-items: center; height: 14.5px; }
  .contact__icon { width: 10px; height: 10px; margin-right: 8px; fill: var(--gold); }
  .contact__address { margin-top: 7px; }
</style>
</head>
<body>
<div class="canvas">

  <section class="card card--back">
    <div class="brand">
      <span class="brand__dot"></span>
      Harborline Crest
      <span class="brand__sub">Insurance Services</span>
    </div>
    <div class="services">
      <span class="services__band services__band--left"></span>
      <span class="services__list">Auto | Home | Business | Life</span>
      <span class="services__band services__band--right"></span>
    </div>
  </section>

  <section class="card card--front">
    <span class="card__tab"></span>
    <div class="person">
      <div class="person__name">Marcus Lane</div>
      <div class="person__role">Managing Director</div>
    </div>
    <div class="brand">
      <span class="brand__dot"></span>
      Harborline Crest
      <span class="brand__sub">Insurance Services</span>
    </div>
    <ul class="contact">
      <li class="contact__item">
        <svg class="contact__icon" viewBox="0 0 10 10"><path d="M1 3.5 Q5 0.5 9 3.5 L8 4.8 L6.6 4.2 L6.6 3.2 Q5 2.6 3.4 3.2 L3.4 4.2 L2 4.8 Z M2.5 5.5 H7.5 L8.5 9.5 H1.5 Z"/></svg>
        +111 555 0142
      </li>
      <li class="contact__item">
        <svg class="contact__icon" viewBox="0 0 10 10"><path d="M0.5 2 H9.5 V8.5 H0.5 Z" fill="var(--gold)"/><path d="M0.8 2.3 L5 5.6 L9.2 2.3" stroke="#0b0b0d" stroke-width="0.9" fill="none"/></svg>
        www.harborlinecrest.com
      </li>
      <li class="contact__item">
        <svg class="contact__icon" viewBox="0 0 10 10"><circle cx="5" cy="5" r="4.5"/><path d="M0.5 5 H9.5 M5 0.5 V9.5 M5 0.6 Q2.2 5 5 9.4 M5 0.6 Q7.8 5 5 9.4" stroke="#0b0b0d" stroke-width="0.7" fill="none"/></svg>
        marcus@harborlinecrest.com
      </li>
      <li class="contact__address">4120 Linden Avenue Pasadena California 91101</li>
    </ul>
  </section>

</div>
</body>
</html>
```